Custom website design and development needed for Davrune , a music and video streaming and download w

Organization or website name
Davrune
Navigation
Artist listing
Top 20 artists
Top 20 songs
Top 20 videos

We are looking to build a website that will allow customers who are music lovers to search,play online or download music or video of their choice as people all around the globe have got a strong fondness for music and the popularity of various singers and musicians proves this point.It should be eye catching and easily navigatable with a nice clean look and feel to it.
Nice to have
Simple logo
Alphabetical sorting of songs by artist
Content Area should contain 3 columns
Top 20 artists
Top 20 songs
Top 20 videos
We need functionality to browse from A to Z in Artist name and music title and search all mp3 in the data base.

Some examples for reference are:

http://tunecrate.example/

https://melovantis.example/

Industry/Entity Type

Artists

Coding

Coded - Design and coding required

```html
<!DOCTYPE html>
<html lang="en">
<head>
<meta charset="utf-8">
<title>Davrune — Music and Video Streaming</title>
<link href="https://fonts.googleapis.com/css2?family=Varela+Round&family=Open+Sans:wght@400;600;700&display=swap" rel="stylesheet">
<style>
:root{
  --page-bg:#f4f4f4;
  --header-bg:#efefef;
  --brand:#8e4a8c;
  --nav-top:#b16cb0;
  --nav-bottom:#7b3a7a;
  --accent:#d21fd0;
  --text-dark:#1e1e1e;
  --text-muted:#555;
  --row-top:#ececec;
  --row-bottom:#cfcfcf;
  --band-top:#f2f2f2;
  --band-bottom:#c9c9c9;
  --footer-bg:#666;
  --footer-text:#eee;
  --white:#fff;
}
*{margin:0;padding:0;box-sizing:border-box}
html,body{width:1200px;height:2426px;overflow:hidden}
body{background:var(--page-bg);font-family:"Open Sans",sans-serif;color:var(--text-dark);position:relative}

.site-header{position:absolute;left:0;top:0;width:1200px;height:86px;background:var(--header-bg)}
.brand{position:absolute;left:62px;top:20px;display:flex;align-items:center;gap:10px;font-family:"Varela Round",sans-serif;font-size:40px;color:var(--brand);letter-spacing:1px;line-height:1}
.brand-dot{width:30px;height:30px;border-radius:50%;background:var(--brand)}
.global-search{position:absolute;left:925px;top:24px;width:217px;height:38px;display:flex;border:1px solid #ddd;background:var(--white)}
.global-search input{flex:1;border:0;padding:0 10px;font:12px "Open Sans",sans-serif;color:#999;background:transparent;outline:none}
.global-search button{width:38px;border:0;border-left:1px solid #ddd;background:var(--white);display:flex;align-items:center;justify-content:center}

.main-nav{position:absolute;left:0;top:86px;width:1200px;height:45px;background:linear-gradient(var(--nav-top),var(--nav-bottom))}
.main-nav a{position:absolute;top:13px;color:var(--white);font-weight:700;font-size:15px;text-decoration:none;letter-spacing:.3px}

.hero{position:absolute;left:0;top:131px;width:1200px;height:456px;background:radial-gradient(ellipse at 45% 10%,#d9c8a6 0%,#9a7e5c 30%,#4a3626 62%,#1a130e 100%)}

.search-band{position:absolute;left:0;top:587px;width:1200px;height:60px;background:linear-gradient(var(--band-top),var(--band-bottom))}
.search-label{position:absolute;top:17px;font-size:20px;color:var(--text-dark)}
.letter-select{position:absolute;left:299px;top:12px;width:52px;height:38px;background:var(--white);border-right:1px solid #ddd;font-size:18px;padding:7px 0 0 12px}
.letter-select svg{position:absolute;right:9px;top:16px}
.field{position:absolute;top:12px;height:38px;background:var(--white)}
.search-btn{position:absolute;top:12px;height:38px;border:0;color:var(--white);font:16px "Open Sans",sans-serif;background:linear-gradient(#a45fa3,#7b3a7a)}

.chart{position:absolute;top:745px;width:330px;height:1548px;background:var(--white)}
.chart h2{height:76px;padding:20px 0 0 21px;font:400 26px "Varela Round",sans-serif;color:var(--accent)}
.chart ol{list-style:none}
.chart li{height:71.5px;position:relative;display:flex;align-items:center}
.chart li:nth-child(odd){background:linear-gradient(var(--row-top),var(--row-bottom))}
.rank{position:absolute;left:13px;font:400 25px "Varela Round",sans-serif;color:var(--accent)}
.thumb{position:absolute;left:55px;width:48px;height:48px}
.t-guitar{background:linear-gradient(135deg,#e3c69a,#a87a4c)}
.t-sunset{background:linear-gradient(#b9a080 0%,#e8632a 45%,#d8521f 100%)}
.t-meadow{background:radial-gradient(circle at 45% 40%,#f2f0c8,#8f9c44 55%,#4e5a26)}
.t-dusk{background:linear-gradient(#a9a59a,#6a5e4c 60%,#3c3428)}
.entry{position:absolute;left:124px}
.artist-name{font-size:14px;font-weight:600;text-transform:uppercase;color:var(--text-dark)}
.track-title{font-size:14px;font-weight:600;color:var(--text-dark);line-height:1.25}
.track-by{font-size:11px;color:var(--text-muted)}

.site-footer{position:absolute;left:0;top:2348px;width:1200px;height:78px;background:var(--footer-bg)}
.footer-links{position:absolute;left:57px;top:22px;display:flex;gap:16px}
.footer-links a{color:var(--footer-text);font-size:13px;text-decoration:none}
.copyright{position:absolute;left:60px;top:48px;font-size:13px;color:#ccc}
.social{position:absolute;left:949px;top:20px;display:flex;gap:6px}
.social span{width:32px;height:32px;border-radius:50%;background:#d9d9d9}
</style>
</head>
<body>

<header class="site-header">
  <div class="brand"><span class="brand-dot"></span>Davrune</div>
  <form class="global-search">
    <input type="text" value="Search All" aria-label="Search all">
    <button type="button" aria-label="Search">
      <svg width="18" height="18" viewBox="0 0 18 18"><circle cx="7.5" cy="7.5" r="5.5" fill="none" stroke="#111" stroke-width="2.2"/><line x1="11.5" y1="11.5" x2="16.5" y2="16.5" stroke="#111" stroke-width="2.6" stroke-linecap="round"/></svg>
    </button>
  </form>
</header>

<nav class="main-nav">
  <a href="#" style="left:63px">HOME</a>
  <a href="#" style="left:150px">EXPLORE</a>
  <a href="#" style="left:259px">ARTIST RADIO</a>
  <a href="#" style="left:404px">GENRES</a>
  <a href="#" style="left:506px">PODCASTS</a>
  <a href="#" style="left:631px">EXCLUSIVES</a>
</nav>

<div class="hero" role="img" aria-label="Concert crowd with raised hands under warm stage lights"></div>

<section class="search-band">
  <span class="search-label" style="left:65px">Search by Artist Name</span>
  <div class="letter-select">A<svg width="10" height="6" viewBox="0 0 10 6"><path d="M0 0h10L5 6z" fill="#bbb"/></svg></div>
  <div class="field" style="left:351px;width:194px"></div>
  <button class="search-btn" style="left:545px;width:82px">Search</button>
  <span class="search-label" style="left:671px">Search by Title</span>
  <div class="field" style="left:826px;width:230px"></div>
  <button class="search-btn" style="left:1056px;width:82px">Search</button>
</section>

<section class="chart" style="left:61px">
  <h2>Top 20 Artists</h2>
  <ol>
    <li><span class="rank">1</span><span class="thumb t-guitar" role="img" aria-label="Artist photo"></span><span class="entry artist-name">Brady Herria</span></li>
    <li><span class="rank">2</span><span class="thumb t-sunset" role="img" aria-label="Artist photo"></span><span class="entry artist-name">Kris Roche</span></li>
    <li><span class="rank">3</span><span class="thumb t-meadow" role="img" aria-label="Artist photo"></span><span class="entry artist-name">Maro Revwsa</span></li>
    <li><span class="rank">4</span><span class="thumb t-dusk" role="img" aria-label="Artist photo"></span><span class="entry artist-name">Brady Herria</span></li>
    <li><span class="rank">5</span><span class="thumb t-guitar" role="img" aria-label="Artist photo"></span><span class="entry artist-name">Kris Roche</span></li>
    <li><span class="rank">6</span><span class="thumb t-meadow" role="img" aria-label="Artist photo"></span><span class="entry artist-name">Maro Revwsa</span></li>
    <li><span class="rank">7</span><span class="thumb t-dusk" role="img" aria-label="Artist photo"></span><span class="entry artist-name">Brady Herria</span></li>
    <li><span class="rank">8</span><span class="thumb t-sunset" role="img" aria-label="Artist photo"></span><span class="entry artist-name">Kris Roche</span></li>
    <li><span class="rank">9</span><span class="thumb t-guitar" role="img" aria-label="Artist photo"></span><span class="entry artist-name">Maro Revwsa</span></li>
    <li><span class="rank">10</span><span class="thumb t-meadow" role="img" aria-label="Artist photo"></span><span class="entry artist-name">Brady Herria</span></li>
    <li><span class="rank">11</span><span class="thumb t-dusk" role="img" aria-label="Artist photo"></span><span class="entry artist-name">Kris Roche</span></li>
    <li><span class="rank">12</span><span class="thumb t-meadow" role="img" aria-label="Artist photo"></span><span class="entry artist-name">Maro Revwsa</span></li>
    <li><span class="rank">13</span><span class="thumb t-dusk" role="img" aria-label="Artist photo"></span><span class="entry artist-name">Brady Herria</span></li>
    <li><span class="rank">14</span><span class="thumb t-sunset" role="img" aria-label="Artist photo"></span><span class="entry artist-name">Kris Roche</span></li>
    <li><span class="rank">15</span><span class="thumb t-guitar" role="img" aria-label="Artist photo"></span><span class="entry artist-name">Maro Revwsa</span></li>
    <li><span class="rank">16</span><span class="thumb t-meadow" role="img" aria-label="Artist photo"></span><span class="entry artist-name">Brady Herria</span></li>
    <li><span class="rank">17</span><span class="thumb t-dusk" role="img" aria-label="Artist photo"></span><span class="entry artist-name">Kris Roche</span></li>
    <li><span class="rank">18</span><span class="thumb t-sunset" role="img" aria-label="Artist photo"></span><span class="entry artist-name">Maro Revwsa</span></li>
    <li><span class="rank">19</span><span class="thumb t-meadow" role="img" aria-label="Artist photo"></span><span class="entry artist-name">Brady Herria</span></li>
    <li><span class="rank">20</span><span class="thumb t-dusk" role="img" aria-label="Artist photo"></span><span class="entry artist-name">Kris Roche</span></li>
  </ol>
</section>

<section class="chart" style="left:437px">
  <h2>Top 20 Songs</h2>
  <ol>
    <li><span class="rank">1</span><span class="thumb t-guitar" role="img" aria-label="Song cover"></span><span class="entry"><div class="track-title">Nulla commodo quam</div><div class="track-by">Haven srls Rows</div></span></li>
    <li><span class="rank">2</span><span class="thumb t-sunset" role="img" aria-label="Song cover"></span><span class="entry"><div class="track-title">Commodo quam nec tortor</div><div class="track-by">Haven srls Rows</div></span></li>
    <li><span class="rank">3</span><span class="thumb t-meadow" role="img" aria-label="Song cover"></span><span class="entry"><div class="track-title">Quam nec tortor</div><div class="track-by">Haven srls Rows</div></span></li>
    <li><span class="rank">4</span><span class="thumb t-dusk" role="img" aria-label="Song cover"></span><span class="entry"><div class="track-title">Nulla commodo quam</div><div class="track-by">Haven srls Rows</div></span></li>
    <li><span class="rank">5</span><span class="thumb t-guitar" role="img" aria-label="Song cover"></span><span class="entry"><div class="track-title">Commodo quam nec tortor</div><div class="track-by">Haven srls Rows</div></span></li>
    <li><span class="rank">6</span><span class="thumb t-meadow" role="img" aria-label="Song cover"></span><span class="entry"><div class="track-title">Quam nec tortor</div><div class="track-by">Haven srls Rows</div></span></li>
    <li><span class="rank">7</span><span class="thumb t-dusk" role="img" aria-label="Song cover"></span><span class="entry"><div class="track-title">Nulla commodo quam</div><div class="track-by">Haven srls Rows</div></span></li>
    <li><span class="rank">8</span><span class="thumb t-sunset" role="img" aria-label="Song cover"></span><span class="entry"><div class="track-title">Commodo quam nec tortor</div><div class="track-by">Haven srls Rows</div></span></li>
    <li><span class="rank">9</span><span class="thumb t-guitar" role="img" aria-label="Song cover"></span><span class="entry"><div class="track-title">Quam nec tortor</div><div class="track-by">Haven srls Rows</div></span></li>
    <li><span class="rank">10</span><span class="thumb t-meadow" role="img" aria-label="Song cover"></span><span class="entry"><div class="track-title">Nulla commodo quam</div><div class="track-by">Haven srls Rows</div></span></li>
    <li><span class="rank">11</span><span class="thumb t-dusk" role="img" aria-label="Song cover"></span><span class="entry"><div class="track-title">Commodo quam nec tortor</div><div class="track-by">Haven srls Rows</div></span></li>
    <li><span class="rank">12</span><span class="thumb t-meadow" role="img" aria-label="Song cover"></span><span class="entry"><div class="track-title">Quam nec tortor</div><div class="track-by">Haven srls Rows</div></span></li>
    <li><span class="rank">13</span><span class="thumb t-dusk" role="img" aria-label="Song cover"></span><span class="entry"><div class="track-title">Nulla commodo quam</div><div class="track-by">Haven srls Rows</div></span></li>
    <li><span class="rank">14</span><span class="thumb t-sunset" role="img" aria-label="Song cover"></span><span class="entry"><div class="track-title">Commodo quam nec tortor</div><div class="track-by">Haven srls Rows</div></span></li>
    <li><span class="rank">15</span><span class="thumb t-guitar" role="img" aria-label="Song cover"></span><span class="entry"><div class="track-title">Quam nec tortor</div><div class="track-by">Haven srls Rows</div></span></li>
    <li><span class="rank">16</span><span class="thumb t-meadow" role="img" aria-label="Song cover"></span><span class="entry"><div class="track-title">Nulla commodo quam</div><div class="track-by">Haven srls Rows</div></span></li>
    <li><span class="rank">17</span><span class="thumb t-dusk" role="img" aria-label="Song cover"></span><span class="entry"><div class="track-title">Commodo quam nec tortor</div><div class="track-by">Haven srls Rows</div></span></li>
    <li><span class="rank">18</span><span class="thumb t-sunset" role="img" aria-label="Song cover"></span><span class="entry"><div class="track-title">Quam nec tortor</div><div class="track-by">Haven srls Rows</div></span></li>
    <li><span class="rank">19</span><span class="thumb t-meadow" role="img" aria-label="Song cover"></span><span class="entry"><div class="track-title">Nulla commodo quam</div><div class="track-by">Haven srls Rows</div></span></li>
    <li><span class="rank">20</span><span class="thumb t-dusk" role="img" aria-label="Song cover"></span><span class="entry"><div class="track-title">Commodo quam nec tortor</div><div class="track-by">Haven srls Rows</div></span></li>
  </ol>
</section>

<section class="chart" style="left:810px">
  <h2>Top 20 Videos</h2>
  <ol>
    <li><span class="rank">1</span><span class="thumb t-guitar" role="img" aria-label="Video still"></span><span class="entry"><div class="track-title">Commodo quam nec tortor</div><div class="track-by">Haven srls Rows</div></span></li>
    <li><span class="rank">2</span><span class="thumb t-sunset" role="img" aria-label="Video still"></span><span class="entry"><div class="track-title">Quam nec tortor</div><div class="track-by">Haven srls Rows</div></span></li>
    <li><span class="rank">3</span><span class="thumb t-meadow" role="img" aria-label="Video still"></span><span class="entry"><div class="track-title">Nulla commodo quam</div><div class="track-by">Haven srls Rows</div></span></li>
    <li><span class="rank">4</span><span class="thumb t-dusk" role="img" aria-label="Video still"></span><span class="entry"><div class="track-title">Commodo quam nec tortor</div><div class="track-by">Haven srls Rows</div></span></li>
    <li><span class="rank">5</span><span class="thumb t-guitar" role="img" aria-label="Video still"></span><span class="entry"><div class="track-title">Quam nec tortor</div><div class="track-by">Haven srls Rows</div></span></li>
    <li><span class="rank">6</span><span class="thumb t-meadow" role="img" aria-label="Video still"></span><span class="entry"><div class="track-title">Nulla commodo quam</div><div class="track-by">Haven srls Rows</div></span></li>
    <li><span class="rank">7</span><span class="thumb t-dusk" role="img" aria-label="Video still"></span><span class="entry"><div class="track-title">Commodo quam nec tortor</div><div class="track-by">Haven srls Rows</div></span></li>
    <li><span class="rank">8</span><span class="thumb t-sunset" role="img" aria-label="Video still"></span><span class="entry"><div class="track-title">Quam nec tortor</div><div class="track-by">Haven srls Rows</div></span></li>
    <li><span class="rank">9</span><span class="thumb t-guitar" role="img" aria-label="Video still"></span><span class="entry"><div class="track-title">Nulla commodo quam</div><div class="track-by">Haven srls Rows</div></span></li>
    <li><span class="rank">10</span><span class="thumb t-meadow" role="img" aria-label="Video still"></span><span class="entry"><div class="track-title">Commodo quam nec tortor</div><div class="track-by">Haven srls Rows</div></span></li>
    <li><span class="rank">11</span><span class="thumb t-dusk" role="img" aria-label="Video still"></span><span class="entry"><div class="track-title">Quam nec tortor</div><div class="track-by">Haven srls Rows</div></span></li>
    <li><span class="rank">12</span><span class="thumb t-meadow" role="img" aria-label="Video still"></span><span class="entry"><div class="track-title">Nulla commodo quam</div><div class="track-by">Haven srls Rows</div></span></li>
    <li><span class="rank">13</span><span class="thumb t-dusk" role="img" aria-label="Video still"></span><span class="entry"><div class="track-title">Commodo quam nec tortor</div><div class="track-by">Haven srls Rows</div></span></li>
    <li><span class="rank">14</span><span class="thumb t-sunset" role="img" aria-label="Video still"></span><span class="entry"><div class="track-title">Quam nec tortor</div><div class="track-by">Haven srls Rows</div></span></li>
    <li><span class="rank">15</span><span class="thumb t-guitar" role="img" aria-label="Video still"></span><span class="entry"><div class="track-title">Nulla commodo quam</div><div class="track-by">Haven srls Rows</div></span></li>
    <li><span class="rank">16</span><span class="thumb t-meadow" role="img" aria-label="Video still"></span><span class="entry"><div class="track-title">Commodo quam nec tortor</div><div class="track-by">Haven srls Rows</div></span></li>
    <li><span class="rank">17</span><span class="thumb t-dusk" role="img" aria-label="Video still"></span><span class="entry"><div class="track-title">Quam nec tortor</div><div class="track-by">Haven srls Rows</div></span></li>
    <li><span class="rank">18</span><span class="thumb t-sunset" role="img" aria-label="Video still"></span><span class="entry"><div class="track-title">Nulla commodo quam</div><div class="track-by">Haven srls Rows</div></span></li>
    <li><span class="rank">19</span><span class="thumb t-meadow" role="img" aria-label="Video still"></span><span class="entry"><div class="track-title">Commodo quam nec tortor</div><div class="track-by">Haven srls Rows</div></span></li>
    <li><span class="rank">20</span><span class="thumb t-dusk" role="img" aria-label="Video still"></span><span class="entry"><div class="track-title">Quam nec tortor</div><div class="track-by">Haven srls Rows</div></span></li>
  </ol>
</section>

<footer class="site-footer">
  <nav class="footer-links">
    <a href="#">Home</a><a href="#">Archives</a><a href="#">All in One Map</a><a href="#">Register</a><a href="#">Login</a>
  </nav>
  <p class="copyright">© 2016 All rights reserved Davrune</p>
  <div class="social" aria-label="Social profiles">
    <span></span><span></span><span></span><span></span><span></span>
  </div>
</footer>

</body>
</html>
```